Flyer-Design für Betreuer von Altenwohn- und Pflegeheimen
Zielgruppe
Die vaxo-pro GmbH betreut Altenwohn- und Pflegeheime im Bereich Arbeitsschutz.
Die Bereiche sind:
- Beratung & Schulung für Arbeitssicherheit, Erste Hilfe und Brandschutz
- Prüfung von Arbeitsmitteln und Medizingeräten
- Reparatur& Wartung von Elektrogeräten
- ein Partner für die 'Lösung aus einer Hand'
Die Zielgruppe sind die Betreiber (Inhaber) und Leitungen von Pflegeeinrichtungen für ältere Menschen und MEnschen mit Behidnerungen
Aufgabenstellung
Das Format soll quadratisch analog dem Logo der vaxo-pro GmbH mit einer Seitenlänge von 210mm sein (Breite DIN A4). Der Folder soll einmal gefaltet sein..
Das Logo beschreibt die Leistungen der vaxo-pro
- linkes oberes Quadrat = 'Beratung&Schulung'
- rechtes oberes Quadrat = 'Prüfung'
- linkes unteres Quadrat = 'Reparatur & Wartung'
- rechtes unteres Quadrat mit dem Haken = 'ein Partner ('...alles aus einer Hand!' <-- wobei mir persönlich diese Wortwahl nicht gefällt')
Der Folder soll auf der ersten Seite beim Leser das Gefühl wecken: 'Das MUSS ich lesen...' <-- Neugierde wecken.
Die beiden Innenseiten sollen die jeweiligen Quadrate der Leistungen beschreiben (siehe oben)
Die Rückseite enthält Angaben zu Referenzen und die Kontaktdaten.
Die Referenzen sollen 'allgemein' gehalten werden:
• kommunale Betreiber
• gemeinnützige Betreiber mit vielen Einrichtungen in ganz Bayern
• viele kleine Einrichtungen mit wenigen Betten ebenso wie
• private große Betreiber mit 1500 Pflegeplätzen und mehr
Karte mit Bullets von Bayern (siehe hochgeladene Datei) - vorerst dieses Bild, in der finalen Version soll diese Karte nicht so sehr nach Plurimo aussehen.
Weieter habe jetzt noch Texte als Word-Datei hinzugefügt...

```html
<!DOCTYPE html>
<html lang="de">
<head>
<meta charset="utf-8">
<title>vaxo-pro Folder</title>
<link href="https://fonts.googleapis.com/css2?family=Montserrat:wght@400;500;800;900&family=Raleway:wght@300;400&display=swap" rel="stylesheet">
<style>
:root{
  --stage:#464646;
  --yellow:#fcc600;
  --white:#ffffff;
  --panel-dark:#6d6d6e;
  --panel-light:#ebebeb;
  --ink:#2a2a2a;
  --text:#4a4a4a;
  --logo-grey:#6d6d6d;
  --art:#e2e2e2;
}
*{margin:0;padding:0;box-sizing:border-box}
html,body{width:1200px;height:1200px;overflow:hidden;background:var(--stage)}
body{position:relative;font-family:"Montserrat",sans-serif;color:var(--text)}
h1,h2{font-weight:400}
.spread{position:absolute;left:58px;width:1092px;height:546px;background:var(--white);overflow:hidden}
.spread-outer{top:35px}
.spread-inner{top:606px}
.abs{position:absolute}

/* outer spread */
.cover-yellow{left:0;top:0;width:946px;height:546px;background:var(--yellow)}
.big-tick{left:0;top:0}
.map-area{left:18px;top:0;width:530px;height:480px;border-radius:0 0 28px 28px;background:linear-gradient(160deg,#ffffff 0%,#fff8dc 100%)}
.references{left:39px;top:0;width:193px;height:166px;background:var(--panel-light);padding:30px 12px 0 26px}
.section-title{font-family:"Raleway",sans-serif;font-weight:400;color:var(--ink);font-size:19px;line-height:1}
.references .section-title{margin-bottom:14px}
.ref-list{list-style:none}
.ref-list li{position:relative;padding-left:14px;font-size:7px;line-height:1.55;color:var(--text);margin-bottom:9px}
.ref-list li::before,.bullet li::before{content:"";position:absolute;left:0;top:2px;width:5px;height:5px;background:var(--yellow)}
.mini-brand{left:252px;top:34px;display:flex;align-items:center;gap:6px;font-size:13px;font-weight:500;color:var(--logo-grey)}
.mini-brand .sq{width:18px;height:18px;background:var(--yellow)}
.headline{left:619px;top:74px;font-family:"Montserrat",sans-serif;font-weight:900;color:var(--white);font-size:17px;line-height:1.3;letter-spacing:.2px}
.contact{left:215px;top:490px;display:flex;gap:10px;font-size:7.4px;line-height:1.5;color:var(--ink);font-style:normal}
.contact .name{font-weight:800}

/* inner spread */
.partner-box{left:0;top:30px;width:223px;height:233px;background:var(--yellow)}
.partner-title{left:41px;top:40px;font-family:"Raleway",sans-serif;font-weight:400;font-size:18.5px;color:var(--ink);white-space:nowrap}
.partner-list{left:41px;top:72px;width:170px;list-style:none}
.partner-list li{font-size:6.8px;font-weight:800;line-height:1.6;color:var(--ink);margin-bottom:11px;text-transform:uppercase}
.art{background:var(--art);border-radius:6px}
.art-partner{left:54px;top:300px;width:216px;height:144px}
.brand{left:318px;top:96px;display:flex;align-items:center;gap:8px}
.brand .sq{width:26px;height:26px;background:var(--yellow)}
.brand .word{font-size:42px;font-weight:500;color:var(--logo-grey);line-height:1;letter-spacing:-1px}
.benefits{left:305px;top:156px;width:212px;height:390px;background:var(--panel-dark);padding:18px 14px 0 22px}
.benefits .section-title{color:var(--yellow);font-size:18px;margin-bottom:14px;padding-left:3px}
.bullet{list-style:none}
.benefits li{position:relative;padding-left:11px;font-size:6.6px;line-height:1.65;color:#f2f2f2;margin-bottom:9.5px}
.bullet b{font-weight:800;text-transform:uppercase}
.svc li{position:relative;padding-left:11px;font-size:6.8px;line-height:1.6;color:var(--text);margin-bottom:10px}
.svc b{display:block;color:var(--ink);font-weight:800;text-transform:uppercase}
.box-light{background:var(--panel-light)}
.pruef-box{left:762px;top:0;width:176px;height:109px}
.pruef-title{left:736px;top:31px}
.pruef-list{left:811px;top:62px;width:215px}
.art-pruef{left:958px;top:27px;width:112px;height:80px}
.art-group{left:579px;top:79px;width:158px;height:164px}
.beratung-box{left:570px;top:255px;width:202px;height:203px}
.beratung-title{left:598px;top:271px}
.beratung-list{left:588px;top:302px;width:180px}
.reparatur-box{left:887px;top:300px;width:205px;height:225px}
.reparatur-title{left:856px;top:315px}
.reparatur-list{left:904px;top:348px;width:180px}
.reparatur-list li{margin-bottom:11px}
.art-repair{left:798px;top:387px;width:84px;height:88px}
.svc-title{font-family:"Raleway",sans-serif;font-weight:400;font-size:19px;line-height:1.1;color:var(--ink);white-space:nowrap}
</style>
</head>
<body>

<section class="spread spread-outer">
  <div class="abs cover-yellow"></div>
  <svg class="abs big-tick" width="1092" height="546" viewBox="0 0 1092 546" aria-hidden="true">
    <polyline points="565,293 766,493 1074,102" fill="none" stroke="#ffffff" stroke-width="70" stroke-linejoin="miter"/>
  </svg>
  <div class="abs map-area" role="img" aria-label="Karte von Bayern mit Standortmarkierungen der betreuten Einrichtungen"></div>
  <div class="abs references">
    <h2 class="section-title">Referenzen</h2>
    <ul class="ref-list">
      <li>kommunale Betreiber</li>
      <li>gemeinnützige Betreiber mit vielen Einrichtungen in ganz Bayern</li>
      <li>viele kleine Einrichtungen mit wenigen Betten ebenso wie private große Betreiber mit 1.500 Pflegeplätzen und mehr</li>
    </ul>
  </div>
  <div class="abs mini-brand"><span class="sq"></span>vaxo-pro</div>
  <h1 class="abs headline">BEI UNS GIBT ES<br>NUR EINEN HAKEN</h1>
  <address class="abs contact">
    <div><span class="name">vaxo-pro GmbH</span><br>Lindenweg 14<br>85600 Talbrunn</div>
    <div>+49 (0) 8000 41270-0<br>info@vaxo-pro.de<br>www.vaxo-pro.de</div>
  </address>
</section>

<section class="spread spread-inner">
  <div class="abs partner-box"></div>
  <h2 class="abs partner-title">Ein Partner – ganzer Service</h2>
  <ul class="abs partner-list">
    <li>Koordination aller Termine<br>und Fälligkeiten</li>
    <li>Reibungslose Prüfabläufe<br>ohne wesentlicher Störung<br>des Tagesgeschäftes</li>
    <li>Wirtschaftliche Mängelbeseitigung</li>
    <li>Inventarisierung durch ein<br>eigenes Kennzeichnungs- und<br>Dokumentationssystem</li>
    <li>VAXO-ONLINE – aktuelle Informationen<br>und Dokumentationen online auf<br>einen Klick</li>
  </ul>
  <div class="abs art art-partner" role="img" aria-label="Gezeichnete Figur mit Stift neben einem großen Haken"></div>

  <div class="abs brand"><span class="sq"></span><span class="word">vaxo-pro</span></div>

  <div class="abs benefits">
    <h2 class="section-title">Ihre Vorteile</h2>
    <ul class="bullet">
      <li><b>Mehr Sicherheit für Mitarbeiter und Bewohner</b> durch geschulten Umgang der Mitarbeiter mit Ihren Medizingeräten</li>
      <li><b>Minimierung der Unfallgefahr</b> und Gewährleistung der Sicherheit Ihrer Mitarbeiter und Bewohner</li>
      <li><b>Detaillierter Überblick</b> zum Ist-Zustand Ihrer technischen Geräte und Anlagen</li>
      <li><b>Steigerung Ihrer Betriebssicherheit</b> durch optimales Erfüllen gesetzlicher, berufsgenossenschaftlicher und versicherungstechnischer Vorgaben</li>
      <li><b>Kostensenkung</b> durch geringere Ausfallzeiten und längere Lebensdauer der Geräte</li>
      <li><b>Erhöhung Ihrer Wirtschaftlichkeit</b> durch klare Zuständigkeiten und straff organisierte, effiziente Prozessabläufe</li>
      <li><b>Kompetente Unterstützung und Hilfe</b> zu vielen Themen und Fragen rund um Ihre Pflegeeinrichtung</li>
      <li><b>Effizienzte und effektive Abwicklung</b> mit einem einzigen Partner für alle Belange</li>
    </ul>
  </div>

  <div class="abs art art-group" role="img" aria-label="Gezeichnete Gruppe vor einer Tafel bei einer Schulung"></div>

  <div class="abs box-light pruef-box"></div>
  <h2 class="abs svc-title pruef-title">Prüfung &amp; Inspektion</h2>
  <div class="abs art art-pruef" role="img" aria-label="Gezeichnete Figur mit Stift und Checkliste"></div>
  <ul class="abs bullet svc pruef-list">
    <li><b>Technische Geräte</b>sicherheitstechnische<br>Überprüfung der aktiven<br>Medizinprodukte / Hilfsmittel</li>
    <li><b>Elektronische Geräte</b>Prüfung der elektrischen Betriebsmittel (Haus- und Küchengeräte, Werkzeuge, bewohnereigene Geräte)</li>
    <li><b>Elektrische Anlagen</b>Prüfung der gesamten elektrischen Anlage inklusive Thermografie (Wärmbildkamera)</li>
    <li><b>Inventarisierung</b>Erstellung eines Bestandsverzeichnisses</li>
    <li><b>Dokumentation</b>Mängelliste und Angebot zur Behebung</li>
  </ul>

  <div class="abs box-light beratung-box"></div>
  <h2 class="abs svc-title beratung-title">Beratung &amp; Schulung</h2>
  <ul class="abs bullet svc beratung-list">
    <li><b>Bedienung</b>Schulung der Mitarbeiter im Umgang mit aktiven Medizinprodukten / Hilfsmitteln</li>
    <li><b>Optimierung</b>Unterstützung bei Themen zum Qualitätsmanagement und zur Prozessgestaltung</li>
    <li><b>Sicherheit</b>Betreuung als externe Fachkraft für Arbeitssicherheit und Brandschutz</li>
  </ul>

  <div class="abs box-light reparatur-box"></div>
  <h2 class="abs svc-title reparatur-title">Reparatur &amp; Wartung</h2>
  <div class="abs art art-repair" role="img" aria-label="Gezeichnete Figur mit Schraubenschlüssel"></div>
  <ul class="abs bullet svc reparatur-list">
    <li>herstellerunabhängiger Service für Medizinprodukte / Hilfsmittel, wie z. B.</li>
    <li>Pflegebetten</li>
    <li>Steckbeckenspülen mit Nachweis der Desinfektionsleitung</li>
    <li>Decken-/Tuch-/Sitzlifter / Aufstehhilfen</li>
    <li>Pflegebadewannen</li>
    <li>Sauerstoffkonzentratoren</li>
    <li>diverse weitere Geräte</li>
  </ul>
</section>

</body>
</html>
```